Etikett für einen Rosé Wein
Zielgruppe
Wir sind ein Weingut und benötigen ein neues Etikett für unseren Muskattrollinger Rosé. Unsere Kunden sind eher traditionelle Weinkäufer.
Aufgabenstellung
Format:
Höhe: 9 cm
Breite: 11 cm
Da es nur ein Vorderetikett gibt, müssen alle relevanten Angaben (Hersteller, Alkohol, Inhalt in L, Rebsorte, etc.) enthalten sein. (siehe Flaschenabbildung anbei)
WÜRTTEMBERG
2019er
Muskattrollinger Rosé
DEUTSCHER QUALITÄTSWEIN
11,0 % Vol.
0,75 l
Enthält Sulfite
A.P.Nr. 58271346
Abfüller
Straße / PLZ / Ort / Tel.
Der Flaschenverschluss ist schwarz d.h. das neue Etikettendesign sollte dazu passen.
Bisher ist der Hintergrund des Weinetiketts schwarz. Dies muss jedoch nicht so bleiben.
Im Anhang finden Sie außerdem ein Plakat. Ggf. können Sie für das Flaschendesign einige nostalgische Elemente davon übernehmen.

```html
<!DOCTYPE html>
<html lang="de">
<head>
<meta charset="utf-8">
<title>Muskattrollinger Rosé – Etikett</title>
<link rel="stylesheet" href="https://fonts.googleapis.com/css2?family=Allura&family=EB+Garamond:wght@400;500;700&display=swap">
<style>
  :root {
    --backdrop: #3a2418;
    --label-white: #ffffff;
    --ink-black: #121212;
    --wine-rust: #b3401c;
    --engraving-grey: #d9d9d9;
  }
  html, body {
    margin: 0;
    padding: 0;
    width: 1100px;
    height: 1200px;
    overflow: hidden;
    background: var(--backdrop);
  }
  .canvas {
    position: relative;
    width: 1100px;
    height: 1200px;
  }
  .wine-label {
    position: absolute;
    left: 50px;
    top: 191px;
    width: 1000px;
    height: 818px;
    background: var(--label-white);
    overflow: hidden;
    font-family: "EB Garamond", Georgia, serif;
    color: var(--ink-black);
  }
  .grape-illustration {
    position: absolute;
    left: 310px;
    top: 0;
    width: 690px;
    height: 740px;
    background:
      radial-gradient(ellipse 42% 38% at 35% 35%, rgba(200,200,200,0.55), rgba(200,200,200,0) 70%),
      radial-gradient(ellipse 38% 45% at 68% 62%, rgba(190,190,190,0.6), rgba(190,190,190,0) 72%);
  }
  .region {
    position: absolute;
    left: 0;
    width: 1000px;
    top: 34px;
    margin: 0;
    text-align: center;
    font-weight: 700;
    font-size: 82px;
    line-height: 1;
    letter-spacing: 1px;
  }
  .vintage {
    position: absolute;
    right: 300px;
    top: 110px;
    margin: 0;
    font-size: 34px;
    line-height: 1;
  }
  .varietal {
    position: absolute;
    left: 250px;
    top: 190px;
    margin: 0;
    font-family: "Allura", cursive;
    font-weight: 400;
    color: var(--wine-rust);
    font-size: 118px;
    line-height: 1;
  }
  .varietal-style {
    position: absolute;
    left: 512px;
    top: 292px;
    margin: 0;
    font-family: "Allura", cursive;
    color: var(--wine-rust);
    font-size: 120px;
    line-height: 1;
  }
  .quality-class {
    position: absolute;
    left: 0;
    width: 1000px;
    top: 490px;
    margin: 0;
    text-align: center;
    font-size: 30px;
    line-height: 44px;
    font-weight: 500;
    letter-spacing: 0.5px;
  }
  .producer-info {
    position: absolute;
    left: 0;
    width: 1000px;
    top: 606px;
    margin: 0;
    text-align: center;
    color: var(--wine-rust);
    font-size: 24px;
    line-height: 38.5px;
    letter-spacing: 0.5px;
  }
  .alcohol {
    position: absolute;
    left: 78px;
    top: 648px;
    margin: 0;
    font-size: 28px;
    line-height: 1;
  }
  .allergen {
    position: absolute;
    left: 80px;
    top: 688px;
    margin: 0;
    color: var(--wine-rust);
    font-size: 21px;
    line-height: 1;
    letter-spacing: 0.5px;
  }
  .volume {
    position: absolute;
    right: 81px;
    top: 676px;
    margin: 0;
    font-size: 36px;
    line-height: 1;
  }
  .address-line {
    position: absolute;
    left: 0;
    width: 1000px;
    top: 750px;
    margin: 0;
    text-align: center;
    font-size: 23px;
    line-height: 1;
    letter-spacing: 0.3px;
  }
  .address-line .dot {
    color: var(--wine-rust);
    padding: 0 4px;
  }
</style>
</head>
<body>
<main class="canvas">
  <section class="wine-label">
    <div class="grape-illustration" role="img" aria-label="Feine graue Gravur einer Weinrebe mit Blatt und Traube"></div>
    <h1 class="region">Württemberg</h1>
    <p class="vintage">2019 er</p>
    <h2 class="varietal">Muskattrollinger</h2>
    <p class="varietal-style">Rosé</p>
    <p class="quality-class">DEUTSCHER<br>QUALITÄTSWEIN</p>
    <p class="producer-info">A.P.Nr. 582 713 46<br>Abfüller D-BWW 582<br>vermarkted durch: Martin Keller</p>
    <p class="alcohol">11,0% Vol.</p>
    <p class="allergen">Enthalten Sulfit</p>
    <p class="volume">0,75 l</p>
    <p class="address-line">Straße 5<span class="dot">•</span>D-74199 Rebenhofen - Kleinsülz<span class="dot">•</span>Tel. 071 34/5829164</p>
  </section>
</main>
</body>
</html>
```